A comprehensive online math curriculum teaching service needs a Landing Page design

We need a Landing Page design for a startup company based in Edmonton, Alberta, Canada, called Trivento Numérica. Trivento Numérica is a comprehensive online math curriculum service for independently schooled students in grades 6-12 worldwide. Instruction is delivered through a one-on-one, virtual, adaptive classroom that uses integrated, interactive digital whiteboards for both teachers and students, with a standard modular lesson workflow for mastering math. Trivento Numérica is designed to help students from all socioeconomic backgrounds master mathematics.

The landing Page should use the same colour scheme as our recently designed PowerPoint template (attached for reference: Design 36712224). Our logo is in the PowerPoint template. I also attached a draft wireframe of our landing page to guide the design.

Target Market(s)

Independently schooled students in grades 6 through 12 worldwide

Industry/Entity Type

Education - Mathematics teaching

Requirements
Must have
• Consistent colours with PowerPoint design

```html
<!DOCTYPE html>
<html lang="en">
<head>
<meta charset="utf-8">
<title>Trivento Numérica – One-on-One Virtual Math Teaching</title>
<link rel="stylesheet" href="https://fonts.googleapis.com/css2?family=Lato:wght@300;400;700;900&display=swap">
<style>
:root{
  --navy:#141f38;
  --navy-2:#1b2847;
  --accent:#4f6fa8;
  --accent-dark:#3d5a8f;
  --ink:#1d2233;
  --text:#3b4050;
  --muted:#5d6272;
  --hero-bg:#eef2f9;
  --soft-bg:#f3f5fa;
  --line:#d7dce8;
  --white:#ffffff;
}
*{box-sizing:border-box;margin:0;padding:0}
html,body{width:1200px;height:3796px;overflow:hidden}
body{font-family:'Lato',sans-serif;color:var(--text);background:var(--white);position:relative}
a{color:inherit;text-decoration:none}

/* header */
.site-header{height:86px;display:flex;align-items:center;padding:0 55px 0 62px;background:var(--white);box-shadow:0 2px 8px rgba(20,31,56,.08);position:relative;z-index:2}
.brand{display:flex;align-items:center;gap:10px}
.brand-dot{width:22px;height:22px;border-radius:50%;background:var(--navy)}
.brand-name{font-size:21px;font-weight:700;color:var(--ink);line-height:1}
.brand-tag{font-size:10px;color:var(--muted);margin-top:5px}
.main-nav{display:flex;gap:38px;margin-left:auto;margin-right:36px;font-size:15px;color:var(--ink)}
.main-nav .active{color:var(--accent);font-weight:700}
.btn{display:inline-flex;align-items:center;justify-content:center;border-radius:6px;font-weight:700;font-size:16px}
.btn-dark{background:var(--navy);color:var(--white)}
.btn-outline{border:2px solid var(--navy);color:var(--navy);background:var(--white)}
.site-header .btn{height:46px;padding:0 20px;font-size:16px}

/* hero */
.hero{height:555px;background:var(--hero-bg);position:relative}
.hero-copy{position:absolute;left:111px;top:88px;width:430px}
.hero-title{font-size:47px;font-weight:400;color:var(--ink);line-height:1.17}
.hero-title strong{font-weight:700}
.hero-lead{margin-top:24px;border-left:2px solid var(--ink);padding-left:16px;font-size:15px;line-height:1.7;color:var(--ink);text-align:justify}
.hero-lead b{font-weight:700}
.hero-actions{margin-top:24px;display:flex;gap:20px}
.hero-actions .btn{height:52px}
.hero-actions .btn-dark{width:184px}
.hero-actions .btn-outline{width:208px}
.hero-illustration{position:absolute;left:600px;top:20px;width:565px;height:510px;border-radius:16px;background:radial-gradient(circle at 40% 50%,#dde5f3,#e8edf7 60%,#eef2f9)}

/* intro band */
.intro{height:639px;background:var(--navy);color:var(--white);position:relative}
.intro-badge{position:absolute;left:111px;top:69px;width:199px;height:199px;border-radius:50%;background:var(--white);display:flex;align-items:center;justify-content:center;text-align:center;color:var(--navy);font-size:22px;font-weight:700;line-height:1.2}
.intro-brand{position:absolute;right:90px;top:60px;text-align:right}
.intro-brand h2{font-size:35px;font-weight:400}
.intro-brand p{font-size:20px;margin-top:16px;font-weight:300}
.intro-strip{position:absolute;left:300px;right:0;top:174px;height:40px;background:var(--accent);display:flex;align-items:center;justify-content:flex-end;padding-right:90px;font-size:15.5px;font-weight:700}
.intro-note{position:absolute;right:90px;top:232px;text-align:right;font-size:14.5px;line-height:2;font-weight:300}
.stats{position:absolute;left:90px;right:90px;top:310px;display:grid;grid-template-columns:repeat(4,1fr);text-align:center}
.stat-value{font-size:58px;font-weight:400;line-height:1}
.stat-label{font-size:16.5px;line-height:1.6;margin-top:14px;font-weight:300}
.intro-body{position:absolute;left:110px;right:110px;top:458px;text-align:center;font-size:15px;line-height:1.75;font-weight:300}

/* section heading */
.section-head{display:flex;align-items:center;gap:14px;font-size:34px;font-weight:400;color:var(--ink)}
.section-head strong{font-weight:700}
.head-dot{width:20px;height:20px;border-radius:50%;background:var(--navy);flex:none}
.head-bar{width:2px;height:34px;background:var(--ink)}

/* proficiency */
.proficiency{height:649px;background:var(--soft-bg);position:relative}
.proficiency-photo{position:absolute;left:111px;top:94px;width:415px;height:453px;border-radius:14px;background:linear-gradient(135deg,#3c77b8,#2c5f9a 50%,#c9a572 100%)}
.proficiency-copy{position:absolute;left:599px;top:82px;width:500px}
.proficiency-copy .lead{font-size:14.5px;font-weight:700;color:var(--ink);margin-top:26px}
.proficiency-copy .intro-text{font-size:14px;line-height:1.8;margin-top:14px;color:var(--text)}
.challenges{margin-top:14px;position:relative}
.challenges::before{content:"";position:absolute;left:20px;top:20px;bottom:40px;border-left:2px dotted var(--accent)}
.challenge{display:flex;gap:16px;margin-bottom:8px;position:relative}
.challenge-icon{width:38px;height:38px;border-radius:50%;background:var(--accent);flex:none;display:flex;align-items:center;justify-content:center;margin-top:4px}
.challenge h3{font-size:14.5px;font-weight:700;color:var(--ink)}
.challenge p{font-size:13.5px;line-height:1.7;color:var(--text);margin-top:4px}
.proficiency-copy .btn{margin-top:8px;height:51px;width:136px;font-size:15px}

/* how it works */
.how{height:702px;background:var(--white);position:relative}
.how .section-head{position:absolute;left:0;right:0;top:70px;justify-content:center}
.how-sub{position:absolute;left:0;right:0;top:140px;text-align:center;font-size:14.5px;color:var(--ink)}
.how-panel{position:absolute;top:193px;width:460px;height:420px;background:var(--white);border-radius:10px;box-shadow:0 2px 14px rgba(20,31,56,.12);padding:22px 28px}
.how-panel.left{left:111px}
.how-panel.right{left:628px}
.how-panel h3{font-size:20px;font-weight:700;color:var(--ink);margin-bottom:20px}
.feature{position:relative;border:1px solid var(--line);border-radius:8px;padding:12px 16px 14px;margin-bottom:20px}
.feature.tall{height:178px}
.feature.short{height:126px}
.feature h4{font-size:15px;font-weight:400;color:var(--accent);margin-bottom:12px}
.feature p{font-size:13px;line-height:1.8;color:var(--text);text-align:justify;padding-right:4px}
.feature-icon{position:absolute;right:-1px;top:-1px;width:60px;height:52px;background:var(--accent);border-radius:0 8px 0 30px;display:flex;align-items:center;justify-content:center}

/* lesson design */
.lessons{height:790px;background:var(--soft-bg);position:relative}
.lessons .section-head{position:absolute;left:0;right:0;top:65px;justify-content:center}
.workflow{position:absolute;top:157px;width:398px;height:540px;background:var(--white);box-shadow:0 2px 12px rgba(20,31,56,.1);padding:16px 20px 0;text-align:center}
.workflow.junior{left:175px}
.workflow.senior{left:628px;height:540px}
.workflow h3{font-size:18px;font-weight:400;color:var(--accent)}
.workflow .grade{font-size:16px;font-weight:700;color:var(--ink);margin-top:8px}
.steps{margin-top:14px;text-align:left}
.step{display:flex;align-items:flex-start;gap:8px;margin-bottom:14px}
.step-num{width:30px;height:30px;border-radius:50%;background:var(--accent);border:3px solid #c9d5ea;color:var(--white);font-size:15px;font-weight:700;display:flex;align-items:center;justify-content:center;flex:none}
.step-main{flex:1;background:var(--white);border-radius:6px;box-shadow:0 1px 6px rgba(20,31,56,.14);padding:7px 9px;display:flex;gap:8px;min-height:82px}
.step-text{flex:1}
.step-head{display:flex;justify-content:space-between;font-size:9px;font-weight:700;color:var(--ink)}
.step-head span{font-weight:400;color:var(--muted);font-size:7.5px}
.step-text p{font-size:7.5px;line-height:1.45;color:var(--muted);margin-top:5px}
.step-side{width:118px;border:1px solid var(--line);border-radius:5px;padding:5px 6px;font-size:6.8px;line-height:1.4;color:var(--muted)}
.step-side b{display:block;font-size:8px;color:var(--ink);margin-bottom:2px}
.step-side em{display:block;font-style:normal;text-align:right;font-weight:700;color:var(--ink);margin-top:2px}
.workflow .btn{position:absolute;left:50%;transform:translateX(-50%);bottom:-3px;height:51px;padding:0 24px;background:var(--accent);color:var(--white);font-size:15px;font-weight:400;border-radius:4px}

/* footer */
.site-footer{height:376px;background:var(--navy);color:var(--white);text-align:center;position:relative}
.footer-brand{position:absolute;left:0;right:0;top:62px;display:flex;justify-content:center;align-items:center;gap:14px}
.footer-brand .brand-dot{width:30px;height:30px;background:var(--white)}
.footer-brand span{font-size:34px;font-weight:700}
.footer-tag{position:absolute;left:0;right:0;top:126px;font-size:15px;font-weight:700}
.footer-nav{position:absolute;left:0;right:0;top:180px;display:flex;justify-content:center;gap:48px;font-size:19px}
.footer-contact{position:absolute;left:0;right:0;top:236px;display:flex;justify-content:center;gap:38px;font-size:19px;align-items:center}
.contact-item{display:flex;align-items:center;gap:14px}
.contact-icon{width:38px;height:38px;border-radius:50%;background:var(--accent);display:flex;align-items:center;justify-content:center}
.copyright{position:absolute;left:0;right:0;top:312px;font-size:15px}
</style>
</head>
<body>

<header class="site-header">
  <a class="brand" href="#">
    <span class="brand-dot"></span>
    <span>
      <div class="brand-name">Trivento Numérica</div>
      <div class="brand-tag">Inspiring Math · Empowering Learning</div>
    </span>
  </a>
  <nav class="main-nav">
    <a class="active" href="#">Home</a>
    <a href="#">Features</a>
    <a href="#">Program</a>
    <a href="#">Tuition</a>
    <a href="#">About Us</a>
    <a href="#">Contact Us</a>
  </nav>
  <a class="btn btn-dark" href="#">Register a Student</a>
</header>

<section class="hero">
  <div class="hero-copy">
    <h1 class="hero-title">Trivento Numérica with <strong>One-on-One Virtual Teaching</strong></h1>
    <p class="hero-lead">Trivento Numérica - accelerated educational outcome is a comprehensive <b>online math curriculum teaching service</b> for independently schooled students in grades <b>6 through 12</b> worldwide.</p>
    <div class="hero-actions">
      <a class="btn btn-dark" href="#">Register a Student</a>
      <a class="btn btn-outline" href="#">Free Consultation</a>
    </div>
  </div>
  <div class="hero-illustration" role="img" aria-label="Illustration of a teacher at a whiteboard showing y = a + bx, linked by dashed arrows to three students at desks"></div>
</section>

<section class="intro">
  <div class="intro-badge">Trivento<br>Numérica</div>
  <div class="intro-brand">
    <h2>Trivento Numérica</h2>
    <p>Accelerated educational outcome</p>
  </div>
  <div class="intro-strip">Registration for Term One math classes opens on June 1, 2026 and closes in the middle of August 2026.</div>
  <p class="intro-note">Trivento Numérica is designed to help students from all socioeconomic backgrounds master mathematics.<br>We teach comprehensive grade 6-12 math curricula to independently schooled students.</p>
  <div class="stats">
    <div><div class="stat-value">90+</div><div class="stat-label">Mastery-based lesson<br>sequence</div></div>
    <div><div class="stat-value">20+</div><div class="stat-label">Homework questions and<br>answers per lesson</div></div>
    <div><div class="stat-value">20+</div><div class="stat-label">Assessment tests per<br>grade program.</div></div>
    <div><div class="stat-value">100%</div><div class="stat-label">One-on-one, virtual<br>adaptive classroom</div></div>
  </div>
  <p class="intro-body">Online, interactive math sessions are delivered in secure virtual classrooms with integrated digital whiteboards for both teacher and student. Real-time one-on-one synchronous math sessions led by qualified experts. We teach modular math lessons that use an incremental development methodology, grounded in continuous practice and review. Our math lessons are designed in small 1 ½-hour units, each covering a new math concept that can be taught in 20 minutes, allowing students ample time to practice the newly introduced math skills daily.</p>
</section>

<section class="proficiency">
  <div class="proficiency-photo" role="img" aria-label="Photo of a hand stacking wooden blocks labelled SKILLS with icons of people, a graduation cap, a light bulb and a target"></div>
  <div class="proficiency-copy">
    <h2 class="section-head"><span class="head-dot"></span><span class="head-bar"></span><span>Our <strong>Proficiency</strong></span></h2>
    <p class="lead">Making math education engaging, effective, and within everyone's reach.</p>
    <p class="intro-text">Teaching math to independently schooled students is not easy.<br>We know the challenges:</p>
    <div class="challenges">
      <div class="challenge">
        <span class="challenge-icon"><svg width="18" height="18" viewBox="0 0 18 18" fill="#fff"><circle cx="5" cy="5" r="2.5"/><circle cx="13" cy="5" r="2.5"/><rect x="2" y="9" width="14" height="6" rx="2"/></svg></span>
        <div><h3>Limited subject expertise</h3><p>Struggling with advanced topics, forgotten knowledge, and specialized methods.</p></div>
      </div>
      <div class="challenge">
        <span class="challenge-icon"><svg width="18" height="18" viewBox="0 0 18 18" fill="#fff"><circle cx="9" cy="7" r="5"/><rect x="6.5" y="12" width="5" height="4" rx="1"/></svg></span>
        <div><h3>Ensuring conceptual understanding</h3><p>Over-reliance on procedures. Bridging the "why" of math and real-world applications.</p></div>
      </div>
      <div class="challenge">
        <span class="challenge-icon"><svg width="18" height="18" viewBox="0 0 18 18" fill="#fff"><rect x="3" y="3" width="12" height="12" rx="2"/><rect x="6" y="6" width="6" height="2" fill="#4f6fa8"/><rect x="6" y="10" width="4" height="2" fill="#4f6fa8"/></svg></span>
        <div><h3>Curriculum challenges</h3><p>How can I choose the right curriculum and supplementary materials?<br>Can I successfully adapt pre-made plans?</p></div>
      </div>
    </div>
    <a class="btn btn-dark" href="#">Read More</a>
  </div>
</section>

<section class="how">
  <h2 class="section-head"><span class="head-dot"></span><span class="head-bar"></span><span>How Trivento Numérica <strong>Works</strong></span></h2>
  <p class="how-sub">Teaching comprehensive math curricula to independently schooled students in grades 6-12 through secure virtual classrooms.</p>
  <div class="how-panel left">
    <h3>Pedagogical Methodology</h3>
    <div class="feature tall">
      <span class="feature-icon"><svg width="24" height="24" viewBox="0 0 24 24" fill="none" stroke="#fff" stroke-width="2"><rect x="5" y="3" width="14" height="18" rx="2"/><path d="M9 8h6M9 12h6M9 16h4"/></svg></span>
      <h4>Effective Curriculum</h4>
      <p>Time-tested and proven pedagogical methodology with three pillars: (1) new math concepts built on previously taught ones; (2) daily review of earlier math concepts to increase understanding; and (3) frequent, cumulative assessments to ensure students master each math skill as new ones are added.</p>
    </div>
    <div class="feature short">
      <span class="feature-icon"><svg width="24" height="24" viewBox="0 0 24 24" fill="none" stroke="#fff" stroke-width="2"><rect x="3" y="5" width="18" height="13" rx="2"/><circle cx="12" cy="11.5" r="3"/></svg></span>
      <h4>Innovative Lesson Design</h4>
      <p>Standard, modular 1½ hour lesson workflows designed to accelerate students' mastery of math skills and concepts.</p>
    </div>
  </div>
  <div class="how-panel right">
    <h3>Virtual Classroom</h3>
    <div class="feature tall">
      <span class="feature-icon"><svg width="24" height="24" viewBox="0 0 24 24" fill="none" stroke="#fff" stroke-width="2"><rect x="3" y="4" width="18" height="13" rx="1"/><path d="M8 21h8M12 17v4"/></svg></span>
      <h4>Personalized Whiteboards</h4>
      <p>Every student gets an individual digital whiteboard, where they can draw, write text and equations, work on practice problems, homework, and tests. The students only see the teacher and their whiteboard.</p>
    </div>
    <div class="feature short">
      <span class="feature-icon"><svg width="24" height="24" viewBox="0 0 24 24" fill="none" stroke="#fff" stroke-width="2"><rect x="8" y="3" width="13" height="10" rx="1"/><circle cx="6" cy="13" r="2.5"/><path d="M2 21c0-3 2-5 4-5s4 2 4 5"/></svg></span>
      <h4>Interactive Sessions</h4>
      <p>Engage with dynamic content, real-time problem solving and feedback, and interactive tools that make math concepts come alive.</p>
    </div>
  </div>
</section>

<section class="lessons">
  <h2 class="section-head"><span class="head-dot"></span><span class="head-bar"></span><span>Innovative <strong>Lesson Design</strong></span></h2>

  <div class="workflow junior">
    <h3>1 and 1/2 Hour Session Lesson Workflow</h3>
    <div class="grade">Grade 6 to 8</div>
    <div class="steps">
      <div class="step"><span class="step-num">1</span><div class="step-main"><div class="step-text"><div class="step-head">PREPARATION <span>15 mins</span></div><p>Promotes mental math and problem-solving and sets the tone for the day's teaching session.</p></div><div class="step-side"><b>Facts Practices</b>Students practice to recall simple math facts quickly.<em>6 min timed</em></div></div></div>
      <div class="step"><span class="step-num">2</span><div class="step-main"><div class="step-text"><div class="step-head">NEW CONCEPTS <span>20 minutes</span></div><p>Introduces new math concepts in small increments.</p></div><div class="step-side"><b>Mental Math</b>Students listen to problems and calculate the answer mentally.<em>4 min timed</em></div></div></div>
      <div class="step"><span class="step-num">3</span><div class="step-main"><div class="step-text"><div class="step-head">LESSON PRACTICE <span>15 minutes</span></div><p>Opportunity for students to practice skills of new math concepts.</p></div><div class="step-side"><b>Lesson Practice</b>Students practice skills of the new math concepts.<em>15 minutes</em></div></div></div>
      <div class="step"><span class="step-num">4</span><div class="step-main"><div class="step-text"><div class="step-head">HOMEWORK <span>40 minutes</span></div><p>Twenty-five to thirty problems to provide students with distributed practice that promotes long term retention of math concepts.</p></div><div class="step-side"><b>Homework</b>Distributed practice that promotes long term retention.<em>40 minutes</em></div></div></div>
    </div>
    <span class="btn">1 hour &amp; 30 min per Session</span>
  </div>

  <div class="workflow senior">
    <h3>1 and 1/2 Hour Session Lesson Workflow</h3>
    <div class="grade">Grade 9 to 12</div>
    <div class="steps">
      <div class="step"><span class="step-num">1</span><div class="step-main"><div class="step-text"><div class="step-head">NEW CONCEPTS <span>25 minutes</span></div><p>Introduces new math concepts in small increments.</p></div><div class="step-side"><b>New Concepts</b>Students practice skills of new math concepts.<em>25 minutes</em></div></div></div>
      <div class="step"><span class="step-num">2</span><div class="step-main"><div class="step-text"><div class="step-head">LESSON PRACTICE <span>20 minutes</span></div><p>Opportunity for students to practice skills of new math concepts.</p></div><div class="step-side"><b>Lesson Practice</b>Students practice skills of new math concepts.<em>20 minutes</em></div></div></div>
      <div class="step"><span class="step-num">3</span><div class="step-main"><div class="step-text"><div class="step-head">HOMEWORK <span>45 minutes</span></div><p>Twenty-five to thirty problems to provide students with distributed practice that promote long-term retention of math concepts.</p></div><div class="step-side"><b>Homework</b>Distributed practice that promotes long-term retention.<em>45 minutes</em></div></div></div>
    </div>
    <span class="btn" style="bottom:auto;top:505px">1 hour &amp; 30 min per Session</span>
  </div>
</section>

<footer class="site-footer">
  <div class="footer-brand"><span class="brand-dot"></span><span>Trivento Numérica</span></div>
  <div class="footer-tag">Inspiring Math · Empowering Learning</div>
  <nav class="footer-nav">
    <a href="#">Home</a><a href="#">Features</a><a href="#">Program</a><a href="#">Tuition</a><a href="#">About Us</a><a href="#">Contact Us</a>
  </nav>
  <div class="footer-contact">
    <span class="contact-item"><span class="contact-icon"><svg width="18" height="14" viewBox="0 0 18 14" fill="none" stroke="#fff" stroke-width="1.6"><rect x="1" y="1" width="16" height="12" rx="1"/><path d="M1 1l8 7 8-7"/></svg></span>hello@triventonumerica.example</span>
    <span class="contact-item"><span class="contact-icon"><svg width="18" height="18" viewBox="0 0 24 24" fill="#fff"><path d="M6.6 10.8a15 15 0 006.6 6.6l2.2-2.2c.3-.3.7-.4 1-.2 1.1.4 2.3.6 3.6.6.6 0 1 .4 1 1V20c0 .6-.4 1-1 1A17 17 0 013 4c0-.6.4-1 1-1h3.5c.6 0 1 .4 1 1 0 1.3.2 2.5.6 3.6.1.3 0 .7-.2 1z"/></svg></span>+1 555 010 0199</span>
  </div>
  <p class="copyright">Copyrights@2026.Trivento Numérica.All Rights Reserved</p>
</footer>

</body>
</html>
```